Webdesign for Hair Company
Marivelle Pure Tresses
Salon & Spa
MarivellePureTresses.example
Our Company believes in celebrating every woman. The ambitious, inventive, energetic and free - We feel women needs to be stimulated to convey their individuality by means of their own individual style-in a manner in which encourages self esteem and allows them to stand out.
Marivelle pure tresses has confidence in individuality. Every person has their particular meaning of perfection. All people have their own individual approach and character, so, why wouldn't you enrich that? If you want to be like someone, it should be only you.
Embrace and establish your personality with your own individual hairstyle. A person's hair is the supreme statement of your identity. Our company consider style as individuality and every person should be able to be seen.
We at Marivelle pure tresses have the final aim to produce an experience that fits our customer’s existence, style and beauty needs. Our mission is always to fulfill consumers with high quality hair merchandise together with beneficial support services. Marivelle Pure tresses recognizes that consumers want genuine, durable and stunning hair. We take our time hand picking each group of imported Indian hair to make sure we sell trusted merchandise.
Friendly
Soft
Gold
Silver/Gray
below header
voriska.example
tundel.example
I need the the front end design for this eCommerce website. No codding is require.
Homepage, product layout, and checkout.
current logo for the website

```html
<!DOCTYPE html>
<html lang="en">
<head>
<meta charset="utf-8">
<title>Marivelle Pure Tresses — Home</title>
<link rel="stylesheet" href="https://fonts.googleapis.com/css2?family=Cinzel:wght@400;600&family=Raleway:wght@300;400&family=Lato:wght@300;400;700&display=swap">
<style>
  :root{
    --ink:#231f20;
    --ink-soft:#2d2a2a;
    --gold:#b8935a;
    --gold-light:#d2b27c;
    --white:#ffffff;
    --grey:#8a8a8a;
    --grey-light:#cfcfcf;
    --text:#333333;
    --hair-dark:#3a2620;
    --hair-mid:#5a3a2e;
  }
  *{box-sizing:border-box;margin:0;padding:0}
  html,body{width:1200px;height:901px;overflow:hidden;background:var(--white)}
  body{font-family:"Lato",sans-serif;color:var(--text);position:relative}

  .topbar{position:absolute;left:0;top:0;width:1200px;height:53px;background:var(--white)}
  .search{position:absolute;left:18px;top:12px;width:178px;height:30px;border:1px solid var(--grey-light);display:flex;align-items:center;padding:0 8px;font-size:10px;color:var(--grey)}
  .search svg{position:absolute;right:8px;top:6px}
  .account-links{position:absolute;right:22px;top:18px;font-size:13px;color:var(--text);display:flex;gap:10px}
  .account-links .sep{color:var(--grey)}

  .masthead{position:absolute;left:0;top:53px;width:1200px;height:154px;background:var(--ink);text-align:center}
  .brand{position:absolute;left:0;right:0;top:50px;font-family:"Cinzel",serif;color:var(--gold)}
  .brand-name{font-size:46px;font-weight:400;letter-spacing:4px;line-height:1}
  .brand-tag{font-size:12px;letter-spacing:5px;margin-top:8px}

  .mainnav{position:absolute;left:0;top:207px;width:1200px;height:61px;display:flex;justify-content:center;align-items:center;gap:26px;font-family:"Raleway",sans-serif;font-weight:300;font-size:23px;color:var(--ink)}
  .mainnav .sep{color:var(--ink)}

  .products{position:absolute;left:140px;top:290px;display:flex;gap:67px}
  .product{width:148px}
  .product-photo{height:210px;display:flex;justify-content:center;align-items:flex-start}
  .hair{background:linear-gradient(180deg,var(--hair-mid),var(--hair-dark) 60%,var(--hair-mid));border-radius:40% 40% 30% 30%}
  .hair.wavy{width:48px;height:200px}
  .hair.straight{width:26px;height:205px;border-radius:30% 30% 10% 10%}
  .hair.curly{width:62px;height:200px}
  .product-title{font-size:10px;font-weight:700;color:var(--ink);margin-top:12px;line-height:1.35;text-transform:uppercase}
  .product-desc{font-size:10px;color:var(--grey);line-height:1.45;margin-top:6px;width:118px}
  .price{font-size:11px;color:var(--ink);margin-top:6px;display:flex;align-items:center;gap:5px}

  .model-photo{position:absolute;left:803px;top:255px;width:397px;height:487px;background:linear-gradient(150deg,#f3efec 0%,#e9e1db 40%,#3a2b25 70%,#1e1614 100%)}

  .newsletter{position:absolute;left:8px;top:698px;display:flex;align-items:center;gap:10px}
  .newsletter-label{font-size:13px;letter-spacing:1px;color:var(--ink)}
  .newsletter-field{width:262px;height:30px;border:1px solid var(--grey-light);display:flex;align-items:center;justify-content:space-between;padding:0 10px;font-size:10px;color:var(--grey)}

  .footer{position:absolute;left:0;top:742px;width:1200px;height:159px;background:var(--ink);color:var(--white);display:flex;justify-content:space-between;padding:0 40px}
  .footer-col{text-align:center;padding-top:30px}
  .footer-col h3{font-family:"Raleway",sans-serif;font-weight:300;font-size:26px;letter-spacing:1px}
  .footer-col h3 span{font-size:14px;vertical-align:middle}
  .footer-col ul{list-style:none;margin-top:12px;font-size:8px;line-height:1.9;color:var(--grey-light);letter-spacing:.5px}
</style>
</head>
<body>

<header class="topbar">
  <div class="search">Search the entire store here
    <svg width="14" height="14" viewBox="0 0 14 14"><circle cx="6" cy="6" r="4.5" fill="none" stroke="#555" stroke-width="1.4"/><line x1="9.5" y1="9.5" x2="13" y2="13" stroke="#555" stroke-width="1.6"/></svg>
  </div>
  <nav class="account-links">
    <span>Log In</span><span class="sep">|</span><span>Checkout</span><span class="sep">|</span><span>My Cart</span><span class="sep">|</span><span>My Account</span><span class="sep">|</span><span>My Cart (0)</span>
  </nav>
</header>

<section class="masthead">
  <div class="brand">
    <div class="brand-name">MARIVELLE</div>
    <div class="brand-tag">PURE TRESSES</div>
  </div>
</section>

<nav class="mainnav">
  <span>Home</span><span class="sep">|</span><span>Straight Hair</span><span class="sep">|</span><span>Wavy Hair</span><span class="sep">|</span><span>Curly Hair</span><span class="sep">|</span><span>Sample</span><span class="sep">|</span><span>Wholesale Request</span>
</nav>

<main class="products">
  <article class="product">
    <div class="product-photo"><div class="hair wavy" role="img" aria-label="Bundle of wavy virgin remy hair"></div></div>
    <h4 class="product-title">Wavy Virgin Remy Hair<br>18 Inches</h4>
    <p class="product-desc">Velora Hair Extensions is imported under the strictest conditions and each bundle of hair comes from one donor to ensure consistency of product.</p>
    <div class="price">$170.00 <svg width="14" height="12" viewBox="0 0 14 12"><path d="M0 1h2.5l2 7h7l2-5H4" fill="none" stroke="#231f20" stroke-width="1.3"/><circle cx="5.5" cy="10.5" r="1.2" fill="#231f20"/><circle cx="10.5" cy="10.5" r="1.2" fill="#231f20"/></svg></div>
  </article>
  <article class="product">
    <div class="product-photo"><div class="hair straight" role="img" aria-label="Bundle of straight virgin remy hair"></div></div>
    <h4 class="product-title">Wavy Virgin Remy Hair<br>18 Inches</h4>
    <p class="product-desc">Velora Hair Extensions is imported under the strictest conditions and each bundle of hair comes from one donor to ensure consistency of product.</p>
    <div class="price">$190.00 <svg width="14" height="12" viewBox="0 0 14 12"><path d="M0 1h2.5l2 7h7l2-5H4" fill="none" stroke="#231f20" stroke-width="1.3"/><circle cx="5.5" cy="10.5" r="1.2" fill="#231f20"/><circle cx="10.5" cy="10.5" r="1.2" fill="#231f20"/></svg></div>
  </article>
  <article class="product">
    <div class="product-photo"><div class="hair curly" role="img" aria-label="Bundle of curly virgin remy hair"></div></div>
    <h4 class="product-title">Wavy Virgin Remy Hair<br>18 Inches</h4>
    <p class="product-desc">Velora Hair Extensions is imported under the strictest conditions and each bundle of hair comes from one donor to ensure consistency of product.</p>
    <div class="price">$170.00 <svg width="14" height="12" viewBox="0 0 14 12"><path d="M0 1h2.5l2 7h7l2-5H4" fill="none" stroke="#231f20" stroke-width="1.3"/><circle cx="5.5" cy="10.5" r="1.2" fill="#231f20"/><circle cx="10.5" cy="10.5" r="1.2" fill="#231f20"/></svg></div>
  </article>
</main>

<div class="model-photo" role="img" aria-label="Woman with long, glossy dark hair"></div>

<section class="newsletter">
  <span class="newsletter-label">SIGN UP FOR OUR NEWSLETTER</span>
  <div class="newsletter-field">Enter Your Email Address
    <svg width="10" height="14" viewBox="0 0 10 14"><path d="M2 1l6 6-6 6" fill="none" stroke="#231f20" stroke-width="2"/></svg>
  </div>
</section>

<footer class="footer">
  <div class="footer-col">
    <h3>ABOUT US <span>&#8964;</span></h3>
    <ul><li>OUR COMMITMENT</li><li>MISSION STATEMENT</li><li>WHY WE CELEBRATE EVERY WOMAN</li></ul>
  </div>
  <div class="footer-col">
    <h3>CUSTOMER SERVICE <span>&#8964;</span></h3>
    <ul><li>SHIPPING &amp; DELIVERY</li><li>RETURNS &amp; EXCHANGES</li><li>CONTACT US</li><li>ORDER TRACKING</li></ul>
  </div>
  <div class="footer-col">
    <h3>PRIVACY POLICY <span>&#8964;</span></h3>
    <ul><li>WHAT WE COLLECT</li><li>WHAT WE DO WITH THE INFORMATION WE GATHER</li><li>SECURITY</li><li>COOKIES</li></ul>
  </div>
</footer>

</body>
</html>
```